Website Design for a holiday home letting busines

We require a redesign of our present website www.birchwoodstays.com. We want the website to stand out and look professional and clean to make holiday hunters want to book a caravan or lodge holiday with us. Our logo is red however we DO NOT want the website to be red. We want a natural colour scheme.

The final design should communicate that we are a professional company to book with.

On the home page we require;
Overview of company
Photo
Search box for holiday (check in)
Late Deals
Reviews
News

We would like the following pages designed; home page, available dates page, caravans page, content page.

The website should be responsive for smart phones. One website I do like is http://www.verdamoro.be/nl/

Target Market(s)

Families

Industry/Entity Type

Travel

Number of Pages Required

5+ page

Font styles to use
Serif

Requirements
Must have
• The project must be responsive for mobile phones and tablets.
• Ability to search for holiday home holidays
• We want a natural colour scheme.
Nice to have
• A style we like is http://www.verdamoro.be/nl/
Should not have
• Do not use red as a colour for the website. Our logo is red so this is the only time we want this used.

```html
<!DOCTYPE html>
<html lang="en">
<head>
<meta charset="utf-8">
<title>Birchwood Stays – Holiday Lodges & Caravans</title>
<link href="https://fonts.googleapis.com/css2?family=Open+Sans:wght@400;600;700&family=Oswald:wght@400;500;600&display=swap" rel="stylesheet">
<style>
:root{
  --green:#6aa83a;
  --green-dark:#4f8a27;
  --navy:#21457c;
  --navy-dark:#183563;
  --blue-btn:#2f6bb3;
  --brand-red:#c8202b;
  --ink:#333;
  --muted:#777;
  --line:#dcdcdc;
  --pale:#eef0ec;
  --footer:#2d2f30;
  --footer-deep:#1f2021;
  --white:#fff;
}
*{box-sizing:border-box;margin:0;padding:0}
html,body{width:1200px;height:2396px;overflow:hidden}
body{font-family:"Open Sans",Arial,sans-serif;color:var(--ink);font-size:13px;background:var(--white)}
.head{font-family:"Oswald",Arial,sans-serif;text-transform:uppercase}

/* header */
.topbar{height:88px;display:flex;align-items:center;justify-content:space-between;padding:0 40px}
.brand{display:flex;align-items:center;gap:12px}
.brand-square{width:34px;height:34px;background:var(--brand-red)}
.brand-name{font-size:24px;font-weight:700;color:#444}
.contact{display:flex;align-items:center;gap:24px}
.contact-lines{display:flex;flex-direction:column;gap:6px;font-weight:600;color:#555}
.contact-lines span{display:flex;align-items:center;gap:8px}
.chat-btn{background:var(--navy);color:var(--white);font-weight:700;padding:10px 18px;font-size:16px;border-radius:3px}
.nav{height:32px;background:var(--navy);display:flex;padding:0 40px}
.nav a{color:var(--white);text-decoration:none;font-size:12px;font-weight:600;padding:0 15px;line-height:32px}
.nav a.active{background:var(--green)}

/* hero */
.hero{position:relative;height:312px;background:linear-gradient(180deg,#9cc4e6 0%,#cfe2ee 38%,#e4e8e2 50%,#8fb56b 68%,#5f8f3c 100%)}
.hero-badge{position:absolute;left:128px;top:58px;width:86px;height:86px;border-radius:50%;background:var(--green);border:4px solid var(--white)}
.hero-panel{position:absolute;right:70px;top:30px;width:300px;height:220px;background:rgba(44,70,40,.72);color:var(--white);padding:24px 22px}
.hero-panel h2{font-size:30px;font-weight:500;line-height:1.1;margin-bottom:14px}
.hero-panel p{font-family:"Oswald",sans-serif;text-transform:uppercase;font-size:15px;line-height:1.35;margin-bottom:18px}
.btn{display:inline-block;color:var(--white);font-weight:700;font-size:12px;text-transform:uppercase;padding:8px 16px;border-radius:2px}
.btn-green{background:var(--green)}
.btn-blue{background:var(--blue-btn)}
.arrow{position:absolute;top:140px;width:28px;height:28px;border-radius:50%;background:rgba(255,255,255,.85);display:flex;align-items:center;justify-content:center}
.hero-tabs{position:absolute;left:0;bottom:0;display:flex}
.hero-tabs span{font-family:"Oswald",sans-serif;color:var(--white);font-size:15px;padding:6px 20px;width:200px}

/* search */
.search{height:88px;display:flex}
.search-form{flex:1;background:var(--pale);padding:12px 40px;display:grid;grid-template-columns:repeat(4,1fr);gap:10px 12px}
.field{height:26px;background:var(--white);border:1px solid var(--line);font-size:11px;color:var(--muted);padding:0 8px;display:flex;align-items:center;justify-content:space-between}
.field::after{content:"";border:4px solid transparent;border-top-color:#888;margin-top:4px}
.check-btn{height:26px;background:var(--navy);color:var(--white);font-size:12px;font-weight:700;display:flex;align-items:center;justify-content:center}
.signup{width:330px;background:var(--green);padding:12px 20px;color:var(--white)}
.signup h3{font-size:16px;font-weight:500;margin-bottom:8px}
.signup-row{display:flex;gap:6px}
.signup-row .input{flex:1;height:24px;background:var(--white)}
.signup-row .sub{background:var(--navy-dark);font-size:11px;font-weight:700;padding:0 10px;line-height:24px}

/* intro */
.intro{height:340px;text-align:center;padding:34px 130px 0}
.intro h1{font-size:28px;font-weight:600;color:#222;margin-bottom:10px}
.intro .lead{font-size:13px;margin-bottom:18px}
.intro h4{font-size:20px;font-weight:600;color:#222;margin-bottom:14px}
.intro p{font-size:12px;line-height:1.7;margin-bottom:12px;color:#444}

/* caravans */
.caravans{position:relative;height:480px;background:linear-gradient(180deg,#a9c6da 0%,#8fae77 35%,#5d8a3a 100%);padding-top:26px}
.ribbon{display:block;width:420px;margin:0 auto;background:var(--green);color:var(--white);text-align:center;font-size:24px;font-weight:500;padding:6px 0;box-shadow:0 2px 0 var(--green-dark)}
.cards{display:flex;gap:22px;justify-content:center;margin-top:34px}
.card{width:240px;background:var(--white)}
.card-photo{height:150px;background:linear-gradient(180deg,#b9d3e6,#e5e5e1 55%,#7ea25a)}
.card-title{background:var(--green);color:var(--white);font-size:16px;padding:5px 10px}
.specs{display:grid;grid-template-columns:1fr 1fr;font-size:10px;padding:8px 10px;gap:4px 8px;color:#555}
.specs b{display:block;color:#222;font-size:11px}
.card-btns{display:flex;gap:6px;padding:4px 10px 12px}
.card-btns .btn{flex:1;text-align:center;font-size:11px;padding:7px 4px;text-transform:none}

/* deals */
.deals{height:400px;padding-top:26px}
.deals .cards{margin-top:26px;gap:40px}
.deal{width:300px;border:1px solid var(--line)}
.deal-photo{position:relative;height:140px;background:linear-gradient(180deg,#c7dbea,#eeeeea 55%,#8aad64)}
.price{position:absolute;right:0;bottom:14px;background:var(--green);color:var(--white);font-weight:700;font-size:15px;padding:4px 14px}
.deal-body{padding:10px 14px}
.deal-body h5{font-size:14px;color:#222}
.deal-body .date{font-size:11px;color:var(--muted);margin:3px 0 8px}
.deal-body .meta{display:flex;justify-content:space-between;font-size:11px;color:#555}
.book{display:block;background:var(--blue-btn);color:var(--white);text-align:center;font-weight:700;font-size:13px;padding:9px 0;margin:10px 14px 14px}

/* feeds */
.feeds{height:380px;background:var(--pale);display:flex;gap:30px;padding:26px 40px}
.feed{flex:1}
.feed h3{font-size:19px;font-weight:500;color:#222;border-bottom:2px solid var(--green);padding-bottom:6px;margin-bottom:14px}
.item{display:flex;gap:10px;margin-bottom:16px}
.thumb{width:70px;height:58px;flex:none;background:linear-gradient(180deg,#b7cfe0,#8fb06a)}
.item h6{font-size:11px;color:var(--navy)}
.item p{font-size:10px;color:#555;line-height:1.45}
.item small{font-size:10px;color:var(--muted)}
.review{margin-bottom:14px;font-size:10px;line-height:1.45;color:#555}
.review b{font-size:11px;color:#222}
.stars{color:var(--green);font-size:11px;letter-spacing:1px}
.social{background:var(--white);border:1px solid var(--line);padding:10px}
.social-top{display:flex;gap:10px;align-items:center;margin-bottom:10px;font-size:11px}
.social-top .sq{width:44px;height:44px;background:var(--green)}
.faces{display:grid;grid-template-columns:repeat(6,1fr);gap:6px}
.faces span{height:42px;background:#c9d3c2}

/* footer */
.footer{height:240px;background:var(--footer);color:#ccc;display:flex;gap:40px;padding:24px 40px}
.footer h3{font-size:16px;font-weight:500;color:var(--white);margin-bottom:12px}
.links{display:grid;grid-template-columns:1fr 1fr;gap:6px 30px;font-size:11px}
.links span::before{content:"› ";color:var(--green)}
.info{font-size:11px;line-height:1.7}
.video{width:300px;height:150px;background:#111;display:flex;align-items:center;justify-content:center}
.bottom{height:36px;background:var(--footer-deep);color:#999;font-size:10px;display:flex;align-items:center;justify-content:space-between;padding:0 40px}
.cards-pay{display:flex;gap:6px}
.cards-pay span{width:30px;height:18px;background:#555;border-radius:2px}
</style>
</head>
<body>

<header class="topbar">
  <div class="brand"><span class="brand-square"></span><span class="brand-name">Birchwood Stays</span></div>
  <div class="contact">
    <div class="contact-lines">
      <span><svg width="14" height="14" viewBox="0 0 24 24"><path fill="#21457c" d="M6.6 10.8a15 15 0 0 0 6.6 6.6l2.2-2.2a1 1 0 0 1 1-.25 11.4 11.4 0 0 0 3.6.6 1 1 0 0 1 1 1V20a1 1 0 0 1-1 1A17 17 0 0 1 3 4a1 1 0 0 1 1-1h3.5a1 1 0 0 1 1 1c0 1.25.2 2.45.6 3.6a1 1 0 0 1-.25 1z"/></svg>Call Now : 01632 960 418</span>
      <span><svg width="14" height="14" viewBox="0 0 24 24"><rect x="2" y="5" width="20" height="14" fill="#21457c"/><path d="M2 5l10 8 10-8" stroke="#fff" stroke-width="2" fill="none"/></svg>info@birchwoodstays.com</span>
    </div>
    <span class="chat-btn">Chat</span>
  </div>
</header>
<nav class="nav">
  <a class="active">Home</a><a>News</a><a>Reviews</a><a>Caravans &amp; Lodges</a><a>2016 Holidays</a><a>2015 Holidays</a><a>Offers</a><a>Payment Plans</a><a>Fernhollow</a><a>Local Attractions</a><a>Contact Us</a>
</nav>

<section class="hero" role="img" aria-label="Family playing on the lawn in front of holiday lodges under a blue sky">
  <span class="hero-badge"></span>
  <div class="arrow" style="left:14px"><svg width="10" height="12"><path d="M8 1L2 6l6 5" stroke="#333" stroke-width="2" fill="none"/></svg></div>
  <div class="arrow" style="right:14px"><svg width="10" height="12"><path d="M2 1l6 5-6 5" stroke="#333" stroke-width="2" fill="none"/></svg></div>
  <div class="hero-panel">
    <h2 class="head">Private Holiday Rentals</h2>
    <p>Quality lodge &amp; caravan breaks at Fernhollow Holiday Park. Book online today!</p>
    <span class="btn btn-green">More details</span>
  </div>
  <div class="hero-tabs">
    <span class="head" style="background:var(--green)">2016 Holidays</span>
    <span class="head" style="background:var(--navy)">2015 Holidays</span>
  </div>
</section>

<section class="search">
  <div class="search-form">
    <span class="field">Caravan type</span><span class="field">Grade</span><span class="field">Sleeps</span><span class="field">Pets</span>
    <span class="field">Bedrooms</span><span class="field">Date</span><span class="field">Nights</span><span class="check-btn">Check availability</span>
  </div>
  <div class="signup">
    <h3 class="head">Sign up for our emails</h3>
    <div class="signup-row"><span class="input"></span><span class="input"></span><span class="sub">Subscribe</span></div>
  </div>
</section>

<section class="intro">
  <h1 class="head">No Deposit Holidays</h1>
  <p class="lead">Would you like to book a 2016 caravan or lodge holiday at Fernhollow Holiday Park?</p>
  <h4 class="head">Pay no deposit?</h4>
  <p>We have flexible low cost monthly and weekly payment plans available from as little as £12 per month by direct debit. This means you can secure your holiday date today without needing a large payment up front and you can spread the cost over the months before you arrive.</p>
  <p>Once you add to the direct debit scheme, payments start within 28 days. You also have the option to choose what day of the week or month the payments are taken from your bank. If you prefer to make a little deposit to secure your dates you can, and the rest is arranged with the balance due before your holiday begins.</p>
  <p>If you have any questions about our hassle free direct debit payment plans please contact us and our friendly team will be more than happy to help.</p>
</section>

<section class="caravans" role="img" aria-label="Holiday park lawn with caravans in the background">
  <h2 class="ribbon head">Our caravans and lodges</h2>
  <div class="cards">
    <article class="card"><div class="card-photo" role="img" aria-label="Caravan exterior"></div><div class="card-title head">The Harlow</div>
      <div class="specs"><span>Caravan type<b>Lodge</b></span><span>Grade<b>Luxury Lodge</b></span><span>Sleeps<b>6</b></span><span>Bedrooms<b>3</b></span></div>
      <div class="card-btns"><span class="btn btn-blue">View details ›</span><span class="btn btn-green">View Prices ›</span></div></article>
    <article class="card"><div class="card-photo" role="img" aria-label="Caravan exterior"></div><div class="card-title head">The Kestrel</div>
      <div class="specs"><span>Caravan type<b>Lodge</b></span><span>Grade<b>Luxury Lodge</b></span><span>Sleeps<b>6</b></span><span>Bedrooms<b>3</b></span></div>
      <div class="card-btns"><span class="btn btn-blue">View details ›</span><span class="btn btn-green">View Prices ›</span></div></article>
    <article class="card"><div class="card-photo" role="img" aria-label="Caravan exterior"></div><div class="card-title head">The Ashdown</div>
      <div class="specs"><span>Caravan type<b>Caravan</b></span><span>Grade<b>Luxury Caravan</b></span><span>Sleeps<b>6</b></span><span>Bedrooms<b>3</b></span></div>
      <div class="card-btns"><span class="btn btn-blue">View details ›</span><span class="btn btn-green">View Prices ›</span></div></article>
  </div>
</section>

<section class="deals">
  <h2 class="ribbon head">Late Deals</h2>
  <div class="cards">
    <article class="deal"><div class="deal-photo" role="img" aria-label="Static caravan on a grass pitch"><span class="price">£275.00</span></div>
      <div class="deal-body"><h5 class="head">The Ashdown</h5><p class="date">Friday 04 September 2015 (3 nights)</p><div class="meta"><span>Sleeps 6</span><span>Bedrooms 3</span></div></div>
      <span class="book">BOOK NOW</span></article>
    <article class="deal"><div class="deal-photo" role="img" aria-label="Static caravan on a grass pitch"><span class="price">£275.00</span></div>
      <div class="deal-body"><h5 class="head">The Ashdown</h5><p class="date">Friday 04 September 2015 (3 nights)</p><div class="meta"><span>Sleeps 6</span><span>Bedrooms 3</span></div></div>
      <span class="book">BOOK NOW</span></article>
    <article class="deal"><div class="deal-photo" role="img" aria-label="Static caravan on a grass pitch"><span class="price">£275.00</span></div>
      <div class="deal-body"><h5 class="head">The Linden 9</h5><p class="date">Friday 04 September 2015 (3 nights)</p><div class="meta"><span>Sleeps 6</span><span>Bedrooms 3</span></div></div>
      <span class="book">BOOK NOW</span></article>
  </div>
</section>

<section class="feeds">
  <div class="feed">
    <h3 class="head">Blog Feed</h3>
    <div class="item"><span class="thumb" role="img" aria-label="Blog photo"></span><div><h6>New lodges arrive for the 2016 season</h6><p>Three new luxury lodges are now on the park and ready to book for spring.</p><small>04 Aug 2015</small></div></div>
    <div class="item"><span class="thumb" role="img" aria-label="Blog photo"></span><div><h6>Summer events at the holiday park</h6><p>Live shows, kids clubs and outdoor fun are running all through August.</p><small>04 Aug 2015</small></div></div>
    <div class="item"><span class="thumb" role="img" aria-label="Blog photo"></span><div><h6>Walks along the nearby coastline</h6><p>Our favourite family walks within a short drive of your holiday home.</p><small>04 Aug 2015</small></div></div>
  </div>
  <div class="feed">
    <h3 class="head">Latest reviews</h3>
    <div class="review"><b>Megan Thornby</b> <span class="stars">★★★★★</span><br>Lovely clean caravan, the kids had a fantastic time and we will be back next year.<br><small>Stayed in The Ashdown</small></div>
    <div class="review"><b>Lorna Pellew</b> <span class="stars">★★★★★</span><br>Great lodge with everything we needed. Booking was easy and the team were helpful.<br><small>Stayed in The Kestrel</small></div>
    <div class="review"><b>Irene Calloway</b> <span class="stars">★★★★★</span><br>Our second stay and it was just as good. Spotless, comfortable and close to the pool.<br><small>Stayed in The Harlow</small></div>
  </div>
  <div class="feed">
    <h3 class="head">Community Feed</h3>
    <div class="social">
      <div class="social-top"><span class="sq"></span><div><b>Birchwood Stays</b><br>1,284 people follow this</div></div>
      <div class="faces"><span></span><span></span><span></span><span></span><span></span><span></span><span></span><span></span><span></span><span></span><span></span><span></span><span></span><span></span><span></span><span></span><span></span><span></span></div>
    </div>
  </div>
</section>

<footer class="footer">
  <div style="width:360px">
    <h3 class="head">Quick Links</h3>
    <div class="links"><span>About us</span><span>Fernhollow</span><span>News</span><span>Local Attractions</span><span>Caravans &amp; Lodges</span><span>Payment Plans</span><span>2016 Holidays</span><span>Contact Us</span><span>2015 Holidays</span><span>Reviews</span><span>Late Deals</span><span>Offers</span></div>
  </div>
  <div style="flex:1">
    <h3 class="head">Contact Information</h3>
    <p class="info">Birchwood Stays Ltd<br>Unit 4, Meadow Court<br>Fernhollow, Northshire<br>NS4 7QD<br>01632 960 418<br>info@birchwoodstays.com</p>
  </div>
  <div>
    <h3 class="head">View Video</h3>
    <div class="video" role="img" aria-label="Holiday park video preview"><svg width="40" height="40" viewBox="0 0 40 40"><circle cx="20" cy="20" r="19" fill="none" stroke="#fff" stroke-width="2"/><path d="M16 12l12 8-12 8z" fill="#fff"/></svg></div>
  </div>
</footer>
<div class="bottom"><span>© 2015 Birchwood Stays. All rights reserved.</span><div class="cards-pay"><span></span><span></span><span></span><span></span></div></div>

</body>
</html>
```